Bay Bolts

I am starting a sharpening service for knives, scissors, and garden tools. It's a sole proprietorship, so it's a small business. The business name is "Bay Bolt." A one or two-page website is fine. Mark Orchard has created a logo for me. There should be pictures of the things I sharpen. There will also be a price list for sharpened items. My address is: 18302 Pellman Way, Larkfield Vale, CA 93560. Phone number is 661-555-0173

```html
<!DOCTYPE html>
<html lang="en">
<head>
<meta charset="utf-8">
<title>Bay Bolt – Knife &amp; Tool Sharpening Service</title>
<link href="https://fonts.googleapis.com/css2?family=Poppins:wght@400;500;600;700&display=swap" rel="stylesheet">
<style>
:root{
  --blue:#173f7f;
  --red:#cc1f1f;
  --black:#0b0b0b;
  --ink:#2a2a2a;
  --muted:#555;
  --pink:#f3d2d2;
  --line:#e2e2e2;
  --white:#fff;
}
*{margin:0;padding:0;box-sizing:border-box}
html,body{width:1200px;height:3987px;overflow:hidden;background:var(--white)}
body{position:relative;font-family:"Poppins",sans-serif;color:var(--ink)}
.abs{position:absolute}
a{color:inherit;text-decoration:none}

/* header */
.brand-panel{position:absolute;left:0;top:0;width:440px;height:124px}
.brand{position:absolute;left:160px;top:36px;font-size:36px;font-weight:700;color:var(--white)}
.contact-chip{position:absolute;top:18px;display:flex;align-items:center;gap:14px}
.chip-icon{width:42px;height:42px;background:var(--red);transform:rotate(45deg);border-radius:6px;display:flex;align-items:center;justify-content:center}
.chip-icon svg{transform:rotate(-45deg)}
.chip-label{font-size:11px;color:var(--muted);line-height:1.2}
.chip-value{font-size:15px;font-weight:600;color:var(--ink)}
.nav{position:absolute;left:418px;top:82px;width:782px;height:42px;background:var(--black);display:flex;align-items:center;padding-left:46px}
.nav a{color:var(--white);font-size:13px;font-weight:500}

/* hero */
.hero-photo{position:absolute;left:0;top:124px;width:1200px;height:620px;
  background:radial-gradient(ellipse at 82% 70%,#f2a23a 0%,#b9621c 18%,rgba(60,35,20,0) 48%),
  linear-gradient(110deg,#161616 0%,#2b2622 45%,#4a3a2c 70%,#2a2624 100%)}
.hero-title{position:absolute;left:158px;top:305px;font-size:43px;font-weight:600;line-height:1.15;color:var(--white)}
.hero-sub{position:absolute;left:160px;top:420px;font-size:14px;line-height:1.1;color:var(--white);letter-spacing:.3px}
.btn{position:absolute;display:flex;align-items:center;justify-content:center;font-size:11px;font-weight:600;text-transform:uppercase;letter-spacing:.3px;clip-path:polygon(12% 0,100% 0,88% 100%,0 100%)}
.btn-red{background:var(--red);color:var(--white)}
.btn-white{background:var(--white);color:var(--red)}

/* section heads */
.eyebrow{position:absolute;font-size:13px;font-weight:500;text-transform:uppercase;color:var(--blue)}
.heading{position:absolute;font-size:33px;font-weight:600;text-transform:uppercase;color:var(--ink);line-height:1}
.center{left:0;width:1200px;text-align:center}
.lead{position:absolute;font-size:13px;line-height:1.5;color:var(--muted)}

.photo{position:absolute}

/* price table */
.price-bg{position:absolute;left:0;top:1520px;width:1200px;height:450px;
  background:linear-gradient(180deg,rgba(255,255,255,1) 0%,rgba(225,225,225,.7) 40%,#9a9a9a 100%)}
.price-table{position:absolute;left:229px;top:1444px;width:742px;height:318px;background:var(--white);border-radius:6px;overflow:hidden}
.pt-head{height:52px;background:var(--pink);display:flex;align-items:center;font-size:14px;color:var(--ink)}
.pt-row{height:53px;display:flex;align-items:center;margin:0 40px;border-bottom:1px solid var(--line);font-size:13px}
.pt-row:last-child{border-bottom:none}
.pt-item{width:491px;display:flex;align-items:center;gap:14px;border-right:1px solid var(--line);height:100%;color:var(--blue)}
.pt-price{padding-left:18px;color:var(--ink)}
.price-note{position:absolute;left:449px;top:1790px;width:302px;height:22px;background:var(--white);border-radius:11px;font-size:11px;color:var(--blue);text-align:center;line-height:22px}

/* services */
.service-card{position:absolute;top:2167px;width:208px;height:268px;background:var(--white)}
.service-card .ph{height:223px}
.service-card p{height:45px;line-height:45px;text-align:center;font-size:15px;font-weight:600;color:var(--ink)}

/* footer */
.foot-brand{position:absolute;left:164px;top:3818px;font-size:36px;font-weight:700;color:var(--white)}
.social{position:absolute;top:3877px;width:16px;height:16px;border-radius:50%;border:2px solid var(--white)}
.foot-title{position:absolute;top:3754px;font-size:16px;font-weight:500;color:var(--white)}
.foot-link{position:absolute;left:565px;font-size:13px;color:var(--white)}
.foot-contact{position:absolute;left:820px;display:flex;align-items:flex-start;gap:14px;font-size:13px;color:var(--white);line-height:1.3}
.foot-icon{width:26px;height:26px;border-radius:50%;background:var(--red);display:flex;align-items:center;justify-content:center;flex:none}
</style>
</head>
<body>

<!-- Header -->
<svg class="brand-panel" viewBox="0 0 440 124"><polygon points="0,0 405,0 438,124 0,124" fill="#173f7f"/></svg>
<div class="brand">Bay Bolt</div>

<div class="contact-chip" style="left:628px">
  <div class="chip-icon"><svg width="18" height="18" viewBox="0 0 24 24"><path fill="#fff" d="M6.6 10.8a15.1 15.1 0 0 0 6.6 6.6l2.2-2.2a1 1 0 0 1 1-.25 11.4 11.4 0 0 0 3.6.57 1 1 0 0 1 1 1V20a1 1 0 0 1-1 1A17 17 0 0 1 3 4a1 1 0 0 1 1-1h3.5a1 1 0 0 1 1 1c0 1.25.2 2.45.57 3.57a1 1 0 0 1-.25 1z"/></svg></div>
  <div><div class="chip-label">Call Us</div><div class="chip-value">661-555-0173</div></div>
</div>
<div class="contact-chip" style="left:812px">
  <div class="chip-icon"><svg width="18" height="18" viewBox="0 0 24 24"><rect x="3" y="6" width="18" height="12" rx="1" fill="#fff"/><path d="M3 7l9 6 9-6" stroke="#cc1f1f" stroke-width="1.6" fill="none"/></svg></div>
  <div><div class="chip-label">E-Mail</div><div class="chip-value">hello@baybolt-sharpening.com</div></div>
</div>

<nav class="nav">
  <a href="#" style="margin-right:54px">Home</a>
  <a href="#" style="margin-right:54px">About Us</a>
  <a href="#" style="margin-right:54px">Services</a>
  <a href="#" style="margin-right:54px">Price</a>
  <a href="#" style="margin-right:46px">Gallery</a>
  <a href="#">Contact Us</a>
</nav>

<!-- Hero -->
<div class="hero-photo" role="img" aria-label="Angle grinder sharpening metal with a spray of orange sparks"></div>
<svg class="abs" style="left:0;top:620px" width="1200" height="130" viewBox="0 0 1200 130">
  <polygon points="0,110 1200,0 1200,130 0,130" fill="#173f7f"/>
  <polygon points="0,118 1200,10 1200,130 0,130" fill="#fff"/>
</svg>
<h1 class="hero-title">Bay Bolt - Knife &amp; Tool<br>Sharpening Service</h1>
<p class="hero-sub">Professinal Sharpening for Knives, scissors, and garden tools,<br>Fast Affordable, Local.</p>
<a class="btn btn-red" href="#" style="left:160px;top:472px;width:152px;height:34px">Call Now</a>

<!-- About -->
<div class="photo" role="img" aria-label="Hands sharpening scissors on a whetstone" style="left:161px;top:821px;width:203px;height:376px;background:linear-gradient(160deg,#5a5450,#2a2826 55%,#8a7a6a)"></div>
<div class="photo" role="img" aria-label="Hands guiding a blade against a bench grinding wheel" style="left:372px;top:821px;width:192px;height:376px;background:linear-gradient(170deg,#d8d2cb,#8a5a34 50%,#5a3a22)"></div>
<div class="eyebrow" style="left:681px;top:862px">Why Choose Us</div>
<h2 class="heading" style="left:681px;top:886px">About Us</h2>
<p class="lead" style="left:681px;top:937px;width:365px;line-height:19.5px">Lorem Ipsum is simply dummy text of the printing and typesetting industry. Lorem Ipsum has been the industry's standard dummy text ever since the 1500s, when an unknown printer took a galley of type and scrambled it to make a type specimen book. It has survived not only five centuries, but also the leap into electronic typesetting, remaining essentially unchanged. It was popularised in the 1960.</p>
<a class="btn btn-red" href="#" style="left:681px;top:1118px;width:152px;height:37px">Call Now</a>

<!-- Prices -->
<div class="price-bg" role="img" aria-label="Faded photo of garden pruners, scissors and a grinding wheel"></div>
<h2 class="heading center" style="top:1312px">Sharpening Prices</h2>
<p class="lead center" style="top:1355px">Lorem Ipsum is simply dummy text of the printing and<br>typesetting industry.</p>
<div class="price-table">
  <div class="pt-head"><span style="padding-left:40px;width:531px">Items</span><span style="padding-left:18px">Price</span></div>
  <div class="pt-row"><div class="pt-item"><svg width="30" height="30" viewBox="0 0 30 30"><path d="M5 5 L22 22" stroke="#173f7f" stroke-width="4" stroke-linecap="round"/><path d="M20 20 L26 26" stroke="#2a2a2a" stroke-width="4" stroke-linecap="round"/></svg>Kitchen Knives</div><div class="pt-price">$50</div></div>
  <div class="pt-row"><div class="pt-item"><svg width="30" height="30" viewBox="0 0 30 30"><circle cx="8" cy="22" r="4" fill="none" stroke="#173f7f" stroke-width="2"/><circle cx="14" cy="25" r="3" fill="none" stroke="#173f7f" stroke-width="2"/><path d="M11 19 L25 5 M16 22 L26 12" stroke="#173f7f" stroke-width="2"/></svg>Scissors &amp; Clippers</div><div class="pt-price">$50</div></div>
  <div class="pt-row"><div class="pt-item"><svg width="30" height="30" viewBox="0 0 30 30"><path d="M4 6 L26 24 M4 24 L26 6" stroke="#173f7f" stroke-width="3" stroke-linecap="round"/></svg>Garden Tools</div><div class="pt-price">$50</div></div>
  <div class="pt-row"><div class="pt-item"><svg width="30" height="30" viewBox="0 0 30 30"><path d="M6 25 L24 7" stroke="#173f7f" stroke-width="5" stroke-linecap="round"/></svg>Mower Blade</div><div class="pt-price">$50</div></div>
  <div class="pt-row"><div class="pt-item"><svg width="30" height="30" viewBox="0 0 30 30"><path d="M8 26 L20 8" stroke="#173f7f" stroke-width="3" stroke-linecap="round"/><rect x="17" y="4" width="9" height="7" fill="#173f7f"/></svg>Axe / Hatchet</div><div class="pt-price">$50</div></div>
</div>
<div class="price-note">Prices May Very Depending on Size &amp; Condition.</div>

<!-- Services band -->
<svg class="abs" style="left:0;top:1890px" width="1200" height="730" viewBox="0 0 1200 730">
  <polygon points="0,78 1200,0 1200,648 0,728" fill="#cc1f1f"/>
</svg>
<div class="eyebrow center" style="top:2015px;color:#fff">Our Services</div>
<h2 class="heading center" style="top:2039px;color:#fff">Services We Offer</h2>
<p class="lead center" style="top:2084px;color:#fff">Lorem Ipsum is simply dummy text of the printing and typesetting industry. Lorem Ipsum has been the<br>industry's standard dummy text ever since the 1500.</p>
<div class="service-card" style="left:260px"><div class="ph" role="img" aria-label="Knife blade held against a grinding wheel" style="background:linear-gradient(150deg,#b8b4ae,#3a3836 60%,#1a1a1a)"></div><p>knives</p></div>
<div class="service-card" style="left:497px"><div class="ph" role="img" aria-label="Blade sharpened on a teal bench grinder with sparks" style="background:linear-gradient(150deg,#2a8c8c,#d8d8d8 50%,#3a3a3a)"></div><p>Scissors</p></div>
<div class="service-card" style="left:733px"><div class="ph" role="img" aria-label="Hands sharpening a garden tool blade on a grinder" style="background:linear-gradient(150deg,#2d6a6e,#8a7055 55%,#2a2a2a)"></div><p>Garden Tools</p></div>
<a class="btn btn-white" href="#" style="left:515px;top:2481px;width:171px;height:38px">Call Now</a>

<!-- Gallery -->
<div class="eyebrow center" style="top:2678px">Gallery</div>
<h2 class="heading center" style="top:2702px">Our Gallery</h2>
<p class="lead center" style="top:2747px">Lorem Ipsum is simply dummy text of the printing and<br>typesetting industry.</p>
<div class="photo" role="img" aria-label="Worker sharpening a wide blade on a grinding wheel" style="left:161px;top:2827px;width:429px;height:300px;background:linear-gradient(140deg,#2d6a6e,#8a7358 55%,#2a2a2a)"></div>
<div class="photo" role="img" aria-label="Hands drawing a chef knife across a whetstone" style="left:608px;top:2827px;width:429px;height:300px;background:linear-gradient(160deg,#2a2826,#6a5a4e 55%,#b8aa98)"></div>
<div class="photo" role="img" aria-label="Yellow angle grinder throwing bright sparks" style="left:161px;top:3142px;width:429px;height:300px;background:radial-gradient(circle at 45% 55%,#f4b040,#9a5a1e 35%,#222 75%)"></div>
<div class="photo" role="img" aria-label="Rotary tool with a grinding stone sharpening a hook blade" style="left:608px;top:3142px;width:429px;height:300px;background:linear-gradient(150deg,#5a4a40,#2a2624 50%,#c07a3a)"></div>
<a class="btn btn-red" href="#" style="left:526px;top:3480px;width:150px;height:37px">Call Now</a>

<!-- Footer -->
<svg class="abs" style="left:0;top:3540px" width="1200" height="447" viewBox="0 0 1200 447">
  <polygon points="0,0 1200,100 1200,447 0,447" fill="#173f7f"/>
  <polygon points="438,40 1200,104 1200,172 438,80" fill="#cc1f1f"/>
  <polygon points="438,80 1200,172 1200,175 438,83" fill="#173f7f"/>
</svg>
<div class="foot-brand">Bay Bolt</div>
<span class="social" style="left:203px"></span>
<span class="social" style="left:246px"></span>
<span class="social" style="left:289px"></span>

<div class="foot-title" style="left:565px">Quick Links</div>
<a class="foot-link" href="#" style="top:3804px">Home</a>
<a class="foot-link" href="#" style="top:3842px">About Us</a>
<a class="foot-link" href="#" style="top:3879px">Services</a>
<a class="foot-link" href="#" style="top:3917px">Contact Us</a>

<div class="foot-title" style="left:820px">Contact Us</div>
<div class="foot-contact" style="top:3806px">
  <span class="foot-icon"><svg width="13" height="13" viewBox="0 0 24 24"><path fill="#fff" d="M6.6 10.8a15.1 15.1 0 0 0 6.6 6.6l2.2-2.2a1 1 0 0 1 1-.25 11.4 11.4 0 0 0 3.6.57 1 1 0 0 1 1 1V20a1 1 0 0 1-1 1A17 17 0 0 1 3 4a1 1 0 0 1 1-1h3.5a1 1 0 0 1 1 1c0 1.25.2 2.45.57 3.57a1 1 0 0 1-.25 1z"/></svg></span>
  <span style="padding-top:5px">661-555-0173</span>
</div>
<div class="foot-contact" style="top:3843px">
  <span class="foot-icon"><svg width="13" height="13" viewBox="0 0 24 24"><rect x="3" y="6" width="18" height="12" rx="1" fill="#fff"/><path d="M3 7l9 6 9-6" stroke="#cc1f1f" stroke-width="1.6" fill="none"/></svg></span>
  <span style="padding-top:5px">baybolt.service@mailbox.net</span>
</div>
<div class="foot-contact" style="top:3880px">
  <span class="foot-icon"><svg width="13" height="13" viewBox="0 0 24 24"><path fill="#fff" d="M12 2a7 7 0 0 0-7 7c0 5 7 13 7 13s7-8 7-13a7 7 0 0 0-7-7zm0 9.5A2.5 2.5 0 1 1 12 6.5a2.5 2.5 0 0 1 0 5z"/></svg></span>
  <span>18302 Pellman Way,<br>Larkfield Vale, CA 93560</span>
</div>

</body>
</html>
```